Verpackungen für Sekt/Champagner Flaschen
Zielgruppe
Dekoration für Hochzeiten. Tisch Dekoration für Hochzeiten. Zielgruppe alles was mit Hochzeiten zutun hat
Aufgabenstellung
Wir lassen gerade ein Tube/Dose herstellen, die als Umverpackung oder einfach Verpackung für Sekt/Champagne Flaschen dienen soll die dann auf die Tische für Hochzeit´s Deko kommt um die die Tisch Deko aufzubessern, statt einfach nur eine Sekt Flasche stehen zu haben. .Die Tube wird komplett in weiß sein und alles andere an Design soll in einem Gold sein. Mr&Mrs oder Just Married mit Herzen und alles was sonst dazu gehört, da lassen wir freie Hand.
Das Design soll Schlicht sein aber auch Luxuriös.
Durchmesser der Tube wird 8,5 cm haben und 34-35 cm sein.
Die Goldene Schrift und das Muster soll am Ende in einem Relief Lack auf der Tube erscheinen

```html
<!DOCTYPE html>
<html lang="en">
<head>
<meta charset="utf-8">
<title>Just Married – Tube Label Band</title>
<link rel="stylesheet" href="https://fonts.googleapis.com/css2?family=Yanone+Kaffeesatz:wght@300;400&display=swap">
<style>
  :root {
    --paper: #ffffff;
    --gold: #a98453;
    --gold-light: #d2b07a;
    --gold-dark: #7d5c32;
    --ink: #151515;
    --panel: #1e2520;
  }
  html, body {
    margin: 0;
    padding: 0;
    width: 1200px;
    height: 292px;
    overflow: hidden;
    background: var(--paper);
  }
  .band {
    position: relative;
    width: 1200px;
    height: 292px;
    background: var(--paper);
    overflow: hidden;
  }
  .stripes {
    position: absolute;
    top: 131px;
    width: 410px;
    height: 43px;
  }
  .stripes--left { left: 0; }
  .stripes--right { left: 790px; }
  .stripe {
    position: absolute;
    left: 0;
    right: 0;
  }
  .stripe--gold-top { top: 0; height: 10px; background: var(--gold); }
  .stripe--ink { top: 16px; height: 10px; background: var(--ink); }
  .stripe--gold-bottom { top: 33px; height: 10px; background: var(--gold); }

  .label {
    position: absolute;
    left: 439px;
    top: 47px;
    width: 323px;
    height: 202px;
    background: var(--panel);
  }
  .crown {
    position: absolute;
    left: 108px;
    top: 13px;
    width: 106px;
    height: 55px;
    background: linear-gradient(180deg, var(--gold-light), var(--gold-dark));
    border-radius: 8px 8px 4px 4px;
  }
  .laurel {
    position: absolute;
    top: 65px;
    width: 36px;
    height: 101px;
    background: linear-gradient(180deg, var(--gold-light), var(--gold-dark));
    border-radius: 18px;
  }
  .laurel--left { left: 41px; }
  .laurel--right { left: 246px; }
  .title {
    position: absolute;
    left: 78px;
    right: 78px;
    top: 71px;
    margin: 0;
    text-align: center;
    font-family: "Yanone Kaffeesatz", "Arial Narrow", sans-serif;
    font-weight: 400;
    font-size: 42px;
    line-height: 45px;
    color: var(--gold);
    white-space: nowrap;
  }
</style>
</head>
<body>
  <main class="band">
    <div class="stripes stripes--left">
      <span class="stripe stripe--gold-top"></span>
      <span class="stripe stripe--ink"></span>
      <span class="stripe stripe--gold-bottom"></span>
    </div>

    <section class="label">
      <div class="crown" role="img" aria-label="Ornate gold crown ornament"></div>
      <div class="laurel laurel--left" role="img" aria-label="Gold laurel branch, left"></div>
      <h1 class="title">Just Married<br>with hearts</h1>
      <div class="laurel laurel--right" role="img" aria-label="Gold laurel branch, right"></div>
    </section>

    <div class="stripes stripes--right">
      <span class="stripe stripe--gold-top"></span>
      <span class="stripe stripe--ink"></span>
      <span class="stripe stripe--gold-bottom"></span>
    </div>
  </main>
</body>
</html>
```